Business Card Design for Occupational Medicine Start Up Company

We need to design a professional business card. We are a healthcare company providing occupational medicine services to blue collar industries. We are professional, efficient and high quality service providers.

Target Market(s)

Blue Collar Industry: Shipbuilding, Ports, Trucking Companies; The Executives and Safety Officers for these companies

Industry/Entity Type

Healthcare

Contact Information for Business Card

Logo, Name, Title, Email, Phone

Other font styles liked:
• Please match our Brand Guide

Requirements
Must have
• Our Company Colors and Logo

```html
<!DOCTYPE html>
<html lang="en">
<head>
<meta charset="utf-8">
<title>Harborline Health — Business Card</title>
<link rel="stylesheet" href="https://fonts.googleapis.com/css2?family=Montserrat:wght@400;500;700;800&display=swap">
<style>
  :root {
    --navy: #2b3483;
    --cyan: #20a7df;
    --orange: #f6b34d;
    --white: #ffffff;
    --ink: #111111;
    --backdrop: #2a2a2a;
  }
  * { box-sizing: border-box; margin: 0; padding: 0; }
  html, body { width: 1200px; height: 1015px; overflow: hidden; }
  body {
    background: var(--backdrop);
    font-family: "Montserrat", sans-serif;
    display: flex;
    flex-direction: column;
    align-items: center;
    justify-content: center;
    gap: 48px;
  }
  .card {
    width: 760px;
    height: 434px;
    position: relative;
    overflow: hidden;
    box-shadow: 0 10px 30px rgba(0,0,0,.5);
  }

  /* Back side */
  .card-back { background: var(--navy); }
  .card-back .brand {
    position: absolute;
    left: 60px;
    bottom: 60px;
  }

  /* Brand lockup */
  .brand { display: flex; align-items: center; gap: 14px; color: var(--white); }
  .brand-dot { width: 22px; height: 22px; border-radius: 50%; background: var(--white); flex: none; }
  .brand-name { font-weight: 700; font-size: 34px; letter-spacing: 2px; text-transform: uppercase; line-height: 1; }

  /* Front side */
  .card-front { background: var(--white); }
  .front-top {
    position: absolute; inset: 0 0 auto 0; height: 226px;
    background: var(--navy);
    display: flex; align-items: center; justify-content: center;
  }
  .front-band {
    position: absolute; left: 0; right: 0; top: 226px; height: 112px;
    background: var(--cyan);
    display: flex; align-items: center; justify-content: center; gap: 26px;
    color: var(--white);
  }
  .person { text-align: right; }
  .person-name { font-weight: 800; font-size: 30px; text-transform: uppercase; line-height: 1.05; }
  .person-title { font-weight: 500; font-size: 19px; }
  .divider { width: 1.5px; height: 74px; background: var(--white); }
  .contacts { list-style: none; font-size: 17px; font-weight: 500; line-height: 1.5; }
  .contacts li { display: flex; align-items: center; gap: 10px; }
  .contacts svg { width: 18px; height: 18px; flex: none; }
  .address {
    position: absolute; left: 0; right: 0; top: 338px; height: 72px;
    display: flex; align-items: center; justify-content: center;
    font-size: 22px; font-weight: 500; color: var(--ink);
  }
  .footer-stripe { position: absolute; left: 0; right: 0; bottom: 0; height: 24px; display: flex; }
  .footer-stripe .navy-part { flex: 1; background: var(--navy); }
  .footer-stripe .orange-part { flex: 1; background: var(--orange); }
</style>
</head>
<body>
  <section class="card card-back" aria-label="Card back">
    <div class="brand">
      <span class="brand-dot"></span>
      <span class="brand-name">Harborline Health</span>
    </div>
  </section>

  <section class="card card-front" aria-label="Card front">
    <div class="front-top">
      <div class="brand">
        <span class="brand-dot"></span>
        <span class="brand-name">Harborline Health</span>
      </div>
    </div>
    <div class="front-band">
      <div class="person">
        <p class="person-name">Daniel Brooks</p>
        <p class="person-title">Managing Director</p>
      </div>
      <span class="divider"></span>
      <ul class="contacts">
        <li>
          <svg viewBox="0 0 24 24" fill="none" stroke="currentColor" stroke-width="2" stroke-linecap="round" stroke-linejoin="round"><path d="M5 3h4l2 5-3 2a12 12 0 0 0 6 6l2-3 5 2v4a2 2 0 0 1-2 2A17 17 0 0 1 3 5a2 2 0 0 1 2-2z"/></svg>
          044-987 654 321
        </li>
        <li>
          <svg viewBox="0 0 24 24" fill="none" stroke="currentColor" stroke-width="2" stroke-linejoin="round"><rect x="2" y="5" width="20" height="14"/><path d="M2 5l10 8 10-8"/></svg>
          hello@harborline.com
        </li>
        <li>
          <svg viewBox="0 0 24 24" fill="none" stroke="currentColor" stroke-width="2"><circle cx="12" cy="12" r="10"/><path d="M2 12h20M12 2c3 3 3 17 0 20M12 2c-3 3-3 17 0 20"/></svg>
          www.harborline.com
        </li>
      </ul>
    </div>
    <p class="address">88 Dockside Road, Port City 20417, Country</p>
    <div class="footer-stripe">
      <span class="navy-part"></span>
      <span class="orange-part"></span>
    </div>
  </section>
</body>
</html>
```